KLT Website Homepage Redesign

My website needs a homepage redesign and banner photos updates for Discovery and SEO Services pages. We sell Search Engine Optimization services. We use Search Engine Optimization techniques to help our clients rank high in search engines like Zorvix. It is an intense competition to consistently rank above other businesses. The problem is there is no easy way to show what the benefits of Search Engine Optimization services look like in an emotional way. I want to use an image from sailboat racing to dramatize that our clients win at Search Engine Optimization marketing.
The following products are desired:
1. Desktop version homepage redesign with a banner that clearly shows we sell Search Engine Optimization services using sailboat racing as a metaphor.
2. Mobile version homepage redesign with a banner that clearly shows we sell Search Engine Optimization services using sailboat racing as a metaphor.
2. New banner photo for the Discovery Page
3. New banner photo for the SEO page
The design must be responsive and show well on desktops, laptops, tablets and mobile phones. The current footer style must be kept. A third service called SEO must be added.
the website URL is www.velmorbix.com
Target Market(s)
Business to Business
Industry/Entity Type
Digital Marketing
Coding
Coded - Design and coding required
Number of Pages Required
1 page
Colors
Designer to choose colors to be used in the design.
Look and feel
Each slider illustrates characteristics of the customer's brand and the style your logo design should communicate.

```html
<!DOCTYPE html>
<html lang="en">
<head>
<meta charset="utf-8">
<title>KLT – Advanced SEO</title>
<link rel="stylesheet" href="https://fonts.googleapis.com/css2?family=Montserrat:wght@800&family=Poppins:wght@400;500;600;700&family=Work+Sans:wght@400;500&family=Lato:wght@400;700&display=swap">
<style>
:root{
  --backdrop:#7ffcec;
  --white:#ffffff;
  --ink:#16161e;
  --muted:#5c6270;
  --nav-ink:#2e2e33;
  --brand-blue:#4a86c7;
  --tint:#eef3fb;
  --accent-blue:#1566e0;
  --accent-orange:#ff5f24;
  --accent-amber:#ffb347;
  --star:#f7a21b;
  --footer-ink:#1f3f95;
  --hero-band:rgba(104,148,212,.72);
}
*{box-sizing:border-box;margin:0;padding:0}
html,body{width:1200px;height:3125px;overflow:hidden}
body{background:var(--backdrop);font-family:"Lato",sans-serif;color:var(--ink);position:relative}
.page{position:absolute;left:64px;top:214px;width:1071px;background:var(--white)}
section,header,footer{position:relative;width:100%;overflow:hidden}

/* header */
.site-header{height:137px;background:var(--white)}
.brand{position:absolute;left:62px;top:40px;display:flex;align-items:center;gap:12px}
.brand-dot{width:22px;height:22px;border-radius:50%;background:var(--brand-blue)}
.brand-name{font-family:"Work Sans",sans-serif;font-weight:500;font-size:48px;color:var(--brand-blue);letter-spacing:2px}
.main-nav{position:absolute;top:74px;left:0;width:100%;font-family:"Work Sans",sans-serif;font-size:20px;letter-spacing:.5px;color:var(--nav-ink)}
.main-nav a{position:absolute;color:inherit;text-decoration:none}
.main-nav a.is-active{color:var(--brand-blue)}

/* hero */
.hero{height:677px}
.hero-photo{position:absolute;inset:0;background:linear-gradient(180deg,#6f9fd6 0%,#8db3dd 30%,#7a8fa6 48%,#2f5b86 56%,#1c4470 75%,#173a62 100%)}
.hero-band{position:absolute;left:0;top:173px;width:100%;height:173px;background:var(--hero-band)}
.hero-title{position:absolute;top:188px;width:100%;text-align:center;font-family:"Montserrat",sans-serif;font-weight:800;font-size:78px;letter-spacing:3px;color:var(--white)}
.hero-sub{position:absolute;top:270px;width:100%;display:flex;justify-content:center;align-items:center;gap:8px;font-family:"Work Sans",sans-serif;font-weight:500;font-size:44px;letter-spacing:3px;color:var(--white)}
.hero-sub::before,.hero-sub::after{content:"";width:57px;height:2px;background:var(--white)}

/* shared section heads */
.eyebrow{position:absolute;width:100%;text-align:center;font-family:"Poppins",sans-serif;font-size:10px;font-weight:500;color:var(--ink)}
.eyebrow span{color:var(--accent-blue);font-size:14px;margin:0 4px}
.eyebrow.warm span{color:var(--accent-orange)}
.section-title{position:absolute;width:100%;text-align:center;font-family:"Poppins",sans-serif;font-weight:700;font-size:28px;line-height:33px;color:var(--ink)}

/* services */
.services{height:537px;background:var(--tint)}
.services .eyebrow{top:48px}
.services .section-title{top:70px}
.services-intro{position:absolute;top:151px;width:100%;text-align:center;font-size:9px;line-height:17px;color:var(--muted)}
.service-card{position:absolute;top:205px;width:151px;height:215px;background:var(--white);border-radius:6px;box-shadow:0 10px 24px rgba(40,70,130,.08);text-align:center;padding:36px 10px 0}
.service-card.is-tall{height:236px}
.service-icon{width:63px;height:63px;border-radius:50%;margin:0 auto 16px;display:flex;align-items:center;justify-content:center}
.service-icon.blue{background:radial-gradient(circle at 35% 30%,#4fa0ff,var(--accent-blue))}
.service-icon.orange{background:radial-gradient(circle at 35% 30%,#ffd04a,var(--accent-orange))}
.service-icon.slate{background:radial-gradient(circle at 35% 30%,#8a93a8,#4b5268)}
.service-name{font-family:"Poppins",sans-serif;font-weight:700;font-size:10px;line-height:13px;margin-bottom:10px}
.service-text{font-size:8.5px;line-height:17px;color:var(--muted)}
.service-link{display:inline-block;margin-top:8px;font-family:"Poppins",sans-serif;font-size:8.5px;font-weight:600;color:#4a2dc9}
.progress{position:absolute;top:481px;left:388px;width:316px;height:8px;border-radius:4px;background:var(--white)}
.progress-fill{width:156px;height:100%;border-radius:4px;background:var(--accent-blue)}

/* testimonials */
.testimonials{height:491px;background:var(--white)}
.testimonials .eyebrow{top:50px}
.testimonials .section-title{top:71px}
.quote-card{position:absolute;top:165px;width:204px;height:154px;background:var(--white);border-radius:4px;box-shadow:0 6px 20px rgba(30,40,80,.1);padding:24px 19px 0;overflow:hidden}
.quote-text{position:relative;font-size:8.2px;line-height:16.8px;color:var(--muted)}
.stars{position:relative;margin-top:6px;color:var(--star);font-size:8px;letter-spacing:3px}
.quote-accent{position:absolute;right:0;bottom:0;width:88px;height:60px;border-top-left-radius:40px;background:linear-gradient(45deg,var(--accent-orange),var(--accent-amber))}
.quote-tail{position:absolute;top:319px;width:0;height:0;border-top:16px solid var(--white);border-right:16px solid transparent;filter:drop-shadow(0 4px 3px rgba(30,40,80,.08))}
.author{position:absolute;top:337px;display:flex;align-items:center;gap:10px}
.author-photo{width:36px;height:36px;border-radius:50%;background:linear-gradient(135deg,#f3c8b8,#d97c6a);border:3px solid var(--white);box-shadow:0 3px 8px rgba(0,0,0,.12)}
.author-name{font-family:"Poppins",sans-serif;font-weight:600;font-size:12px;color:var(--ink)}
.author-role{font-family:"Poppins",sans-serif;font-size:7.5px;color:var(--muted)}
.slider-arrow{position:absolute;top:407px;width:29px;height:29px;border-radius:50%;display:flex;align-items:center;justify-content:center;box-shadow:0 3px 8px rgba(0,0,0,.12)}
.slider-arrow.prev{left:500px;background:var(--accent-blue)}
.slider-arrow.next{left:544px;background:var(--white)}

/* contact */
.contact{height:531px;background:var(--tint)}
.contact .eyebrow{top:53px}
.contact .section-title{top:73px}
.field{position:absolute;height:25px;background:var(--white);border-radius:2px;font-size:7px;color:#8a8f9c;padding:8px 14px}
.field.message{height:75px}
.send-button{position:absolute;left:382px;top:371px;width:303px;height:32px;border-radius:3px;background:linear-gradient(90deg,var(--accent-orange),var(--accent-amber));box-shadow:0 6px 14px rgba(255,120,40,.3);display:flex;align-items:center;justify-content:center;gap:5px;font-family:"Poppins",sans-serif;font-size:8px;font-weight:600;color:var(--white)}

/* footer */
.site-footer{height:324px;font-family:"Work Sans",sans-serif;color:var(--footer-ink)}
.footer-photo{position:absolute;inset:0;background:linear-gradient(180deg,#c9d6ea 0%,#d6e0ef 45%,#b7c7de 70%,#a9bcd6 100%)}
.footer-head{position:absolute;top:40px;font-size:22px;font-weight:400;letter-spacing:3px;transform:translateX(-50%);white-space:nowrap}
.footer-block{position:absolute;font-size:17px;line-height:21px}
.footer-links{position:absolute;top:86px;list-style:none;font-size:17px}
.footer-links li{height:30px}
.copyright{position:absolute;top:246px;width:100%;text-align:center;font-size:16px}
</style>
</head>
<body>
<div class="page">

  <header class="site-header">
    <div class="brand"><span class="brand-dot"></span><span class="brand-name">KLT</span></div>
    <nav class="main-nav">
      <a class="is-active" style="left:512px">Home</a>
      <a style="left:613px">Seo</a>
      <a style="left:693px">Info</a>
      <a style="left:773px">Let’s talk</a>
      <a style="left:914px">Support</a>
    </nav>
  </header>

  <section class="hero">
    <div class="hero-photo" role="img" aria-label="Two racing sailboats with crews heeling on open sea under a blue sky, coastline behind"></div>
    <div class="hero-band"></div>
    <h1 class="hero-title">ADVANCED SEO</h1>
    <p class="hero-sub">TAKE THE LEAD</p>
  </section>

  <section class="services">
    <p class="eyebrow"><span>{</span>Fetaured service<span>}</span></p>
    <h2 class="section-title">Additional Services that will<br>Grow Your Business</h2>
    <p class="services-intro">As a SEO Advisor or web crawler expert, I help organizations adjust to<br>the expanding significance of internet promoting.</p>

    <article class="service-card is-tall" style="left:295px">
      <div class="service-icon blue"><svg width="28" height="28" viewBox="0 0 28 28"><circle cx="14" cy="14" r="7" fill="none" stroke="#fff" stroke-width="3"/><g stroke="#fff" stroke-width="3"><path d="M14 2v5M14 21v5M2 14h5M21 14h5M5.5 5.5l3.5 3.5M19 19l3.5 3.5M5.5 22.5L9 19M19 9l3.5-3.5"/></g></svg></div>
      <h3 class="service-name">SEO AUDIT</h3>
      <p class="service-text">Zorvix Ad campaigns are an effective way to target receptive audience they get you.</p>
      <span class="service-link">Contact us →</span>
    </article>
    <article class="service-card" style="left:462px">
      <div class="service-icon orange"><svg width="26" height="24" viewBox="0 0 26 24" fill="#fff"><rect x="2" y="14" width="4" height="8"/><rect x="8" y="10" width="4" height="12"/><rect x="14" y="12" width="4" height="10"/><rect x="20" y="6" width="4" height="16"/><path d="M2 10l7-6 6 4 8-7" stroke="#fff" stroke-width="2" fill="none"/></svg></div>
      <h3 class="service-name">SEO Consulting</h3>
      <p class="service-text">Make sure your brand assets contribute to your company’s personality and reputation.</p>
    </article>
    <article class="service-card" style="left:628px">
      <div class="service-icon slate"><svg width="28" height="28" viewBox="0 0 28 28" fill="none" stroke="#fff" stroke-width="2"><circle cx="14" cy="14" r="5"/><circle cx="5" cy="5" r="2.5"/><circle cx="23" cy="5" r="2.5"/><circle cx="5" cy="23" r="2.5"/><circle cx="23" cy="23" r="2.5"/><path d="M7 7l3.5 3.5M21 7l-3.5 3.5M7 21l3.5-3.5M21 21l-3.5-3.5"/></svg></div>
      <h3 class="service-name">Website Design,<br>Development &amp; Hosting</h3>
      <p class="service-text">Your content is an integral part of your SEO efforts and online marketing strategy.</p>
    </article>
    <div class="progress"><div class="progress-fill"></div></div>
  </section>

  <section class="testimonials">
    <p class="eyebrow"><span>{</span>Testimonials<span>}</span></p>
    <h2 class="section-title">We serve our clients with the<br>best of our capacity</h2>

    <article class="quote-card" style="left:211px">
      <span class="quote-accent" role="img" aria-label="Orange accent shape in the card corner"></span>
      <p class="quote-text">Lorem ipsum dolor sit amet consecter tony adipiscing elitsed do eiusmodi tempor roar incididunt ut laboreet dolore magna as the opposed to using. Type of partnership or Malta. The limited todot liability.</p>
      <p class="stars">★★★★★</p>
    </article>
    <div class="quote-tail" style="left:211px"></div>
    <div class="author" style="left:224px"><span class="author-photo" role="img" aria-label="Client portrait"></span><div><p class="author-name">Tavia Morel</p><p class="author-role">SEO Manager</p></div></div>

    <article class="quote-card" style="left:435px">
      <p class="quote-text">Lorem ipsum dolor sit amet consecter tony adipiscing elitsed do eiusmodi tempor roar incididunt ut laboreet dolore magna as the opposed to using. Type of partnership or Malta. The limited todot liability.</p>
      <p class="stars">★★★★★</p>
    </article>
    <div class="quote-tail" style="left:435px"></div>
    <div class="author" style="left:449px"><span class="author-photo" role="img" aria-label="Client portrait"></span><div><p class="author-name">Corin Salbe</p><p class="author-role">SEO Manager</p></div></div>

    <article class="quote-card" style="left:657px">
      <p class="quote-text">Lorem ipsum dolor sit amet consecter tony adipiscing elitsed do eiusmodi tempor roar incididunt ut laboreet dolore magna as the opposed to using. Type of partnership or Malta. The limited todot liability.</p>
      <p class="stars">★★★★★</p>
    </article>
    <div class="quote-tail" style="left:657px"></div>
    <div class="author" style="left:676px"><span class="author-photo" role="img" aria-label="Client portrait"></span><div><p class="author-name">Idra Pollen</p><p class="author-role">SEO Manager</p></div></div>

    <span class="slider-arrow prev"><svg width="14" height="10" viewBox="0 0 14 10" fill="none" stroke="#fff" stroke-width="1.6"><path d="M13 5H1M5 1L1 5l4 4"/></svg></span>
    <span class="slider-arrow next"><svg width="14" height="10" viewBox="0 0 14 10" fill="none" stroke="#16161e" stroke-width="1.6"><path d="M1 5h12M9 1l4 4-4 4"/></svg></span>
  </section>

  <section class="contact">
    <p class="eyebrow warm"><span>{</span>Contact us<span>}</span></p>
    <h2 class="section-title">Want to hire us to boost site<br>contact us any time!</h2>
    <div class="field" style="left:382px;top:192px;width:143px">First name *</div>
    <div class="field" style="left:541px;top:192px;width:143px">Last name *</div>
    <div class="field" style="left:382px;top:236px;width:143px">Your mail *</div>
    <div class="field" style="left:541px;top:236px;width:143px">Phone number *</div>
    <div class="field message" style="left:382px;top:279px;width:302px">Message...</div>
    <div class="send-button"><svg width="9" height="9" viewBox="0 0 10 10"><circle cx="5" cy="5" r="5" fill="#fff"/><path d="M3 5h4M5.5 3.5L7 5 5.5 6.5" stroke="#ff7a30" fill="none"/></svg>Send now</div>
  </section>

  <footer class="site-footer">
    <div class="footer-photo" role="img" aria-label="Faded view of a sailboat fleet racing on the water"></div>
    <h2 class="footer-head" style="left:292px">TAKE THE LEAD</h2>
    <h2 class="footer-head" style="left:780px">USEFUL LINKS</h2>
    <p class="footer-block" style="left:64px;top:86px">Contact Us</p>
    <p class="footer-block" style="left:64px;top:117px">418 Harborline Way<br>Suite 12B<br>Marlow Bay, MD 20990</p>
    <ul class="footer-links" style="left:552px"><li>Home</li><li>Web Strategy</li><li>Support</li><li>Privacy</li></ul>
    <ul class="footer-links" style="left:780px"><li>SEO</li><li>Advanced Website Tools</li><li>Testimonials</li><li>Terms of Use</li></ul>
    <p class="copyright">© 2019 KLT | All Rights Reserved | Web Strategy by KLT</p>
  </footer>

</div>
</body>
</html>
```